Front Yard Sign for Real Estate Company

Bright Porch Keys is a brand new real estate broker. We need signs to put in front yard of houses that we are selling. 3D would be great. I have included the company LOGO

Target Market(s)

Residential Property buyers and sellers

Industry/Entity Type

Real Estate

Colors
ec1f27
ffc214
fbed22
ffffff

Requirements
Must have
• 3D look would be great. Logo must be included in the yard signs.
• Must include phone # to call: 614-290-4417

```html
<!DOCTYPE html>
<html lang="en">
<head>
<meta charset="utf-8">
<title>Bright Porch Keys – Yard Sign</title>
<link href="https://fonts.googleapis.com/css2?family=Montserrat:wght@800;900&family=Oswald:wght@500&family=Poppins:ital,wght@1,500&display=swap" rel="stylesheet">
<style>
  :root {
    --brand-red: #ec1f27;
    --brand-yellow: #ffc214;
    --brand-gold: #c99a2e;
    --rule-gold: #d0a33a;
    --sign-white: #ffffff;
    --backdrop: #ffffff;
    --shadow-grey: rgba(0,0,0,0.18);
  }
  html, body {
    margin: 0;
    width: 1200px;
    height: 900px;
    overflow: hidden;
    background: var(--backdrop);
  }
  .canvas {
    position: relative;
    width: 1200px;
    height: 900px;
  }
  .yard-sign {
    position: absolute;
    left: 320px;
    top: 40px;
    width: 560px;
    height: 820px;
    background: var(--sign-white);
    box-shadow: 0 2px 14px var(--shadow-grey);
  }
  .brand-row {
    position: absolute;
    top: 180px;
    left: 0;
    width: 100%;
    display: flex;
    justify-content: center;
    align-items: center;
    gap: 14px;
  }
  .brand-dot {
    width: 34px;
    height: 34px;
    border-radius: 50%;
    background: var(--brand-yellow);
  }
  .brand-name {
    font-family: "Montserrat", sans-serif;
    font-weight: 800;
    font-size: 42px;
    color: var(--brand-red);
    letter-spacing: -0.5px;
  }
  .headline {
    position: absolute;
    left: 62px;
    margin: 0;
    font-family: "Montserrat", sans-serif;
    font-weight: 900;
    line-height: 1;
    letter-spacing: 2px;
  }
  .headline-for {
    top: 300px;
    font-size: 158px;
    color: var(--brand-yellow);
  }
  .headline-sell {
    top: 420px;
    font-size: 158px;
    color: var(--brand-red);
    letter-spacing: 0;
  }
  .pointer-arrow {
    position: absolute;
    left: 480px;
    top: 326px;
  }
  .ground-shadow {
    position: absolute;
    left: 140px;
    top: 596px;
    width: 280px;
    height: 10px;
    border-radius: 50%;
    background: radial-gradient(ellipse at center, rgba(0,0,0,0.28), rgba(0,0,0,0) 70%);
  }
  .phone {
    position: absolute;
    top: 628px;
    left: 0;
    width: 100%;
    text-align: center;
    font-family: "Oswald", sans-serif;
    font-weight: 500;
    font-size: 86px;
    line-height: 1;
    color: var(--brand-red);
    letter-spacing: 1px;
  }
  .web-row {
    position: absolute;
    top: 732px;
    left: 70px;
    width: 420px;
    display: flex;
    align-items: center;
    gap: 14px;
  }
  .rule {
    flex: 1;
    height: 2px;
    background: var(--rule-gold);
  }
  .website {
    font-family: "Poppins", sans-serif;
    font-style: italic;
    font-weight: 500;
    font-size: 20px;
    color: var(--brand-red);
    white-space: nowrap;
  }
</style>
</head>
<body>
<main class="canvas">
  <section class="yard-sign">
    <div class="brand-row">
      <span class="brand-dot"></span>
      <span class="brand-name">Bright Porch Keys</span>
    </div>

    <h1 class="headline headline-for">FOR</h1>
    <h1 class="headline headline-sell">SELL</h1>

    <svg class="pointer-arrow" width="44" height="192" viewBox="0 0 44 192" aria-hidden="true">
      <polygon points="0,0 44,96 0,192" fill="var(--brand-gold)"/>
    </svg>

    <div class="ground-shadow"></div>

    <div class="phone">614 290 4417</div>
    <div class="web-row">
      <span class="rule"></span>
      <span class="website">brightPorchKeys.com</span>
      <span class="rule"></span>
    </div>
  </section>
</main>
</body>
</html>
```